Human Resource Consulting practice needs a business card design

We need a business card design (double sided colour) for our Human Resource (HR) consulting practice in regional New South Wales, australia. Our business name is Staffwise Partners. We support small and medium business across the Mid North Coast of New South Wales by providing them with outsourced HR support, services and products to help them achieve compliance with workplace legislation and across all areas of the employment lifecycle from recruitment to termination and everything in between. Our corporate colours are hot pink and black. The final design should communicate professionalism, trust, people focus.
I have attached the current (old) business card for your reference.

Target Market(s)

Business owners and high level managers

Industry/Entity Type

Business

Contact Information for Business Card

Name
Title
Phone no
Mobile no
Address
PO Box
email address
website

Colors
e34197

Requirements
Must have
• Tempate for changing business card personal details including Name, position title, mobile number, email address.
• Keep current logo and colours as per attached
• Logo must be presented in 2 colours or black only not white
Nice to have
• One side logo and graphic only other side logo and personal details
Should not have
• Should not be the same as the current version (attached) but a modern interpretation.
• Does not need a busy reverse side with our list of services as per current version. I feel this is too busy.
• No photos

```html
<!DOCTYPE html>
<html lang="en">
<head>
<meta charset="utf-8">
<title>Staffwise Partners – Business Card</title>
<link rel="stylesheet" href="https://fonts.googleapis.com/css2?family=Open+Sans:wght@400;600;700&display=swap">
<style>
  :root {
    --hot-pink: #e0168e;
    --pink-light: #e34197;
    --pink-deep: #c80a7c;
    --ink: #1c1c1c;
    --grey-text: #4a4a4a;
    --card-white: #f6f6f6;
    --backdrop: #e9e6e3;
  }
  * { box-sizing: border-box; margin: 0; padding: 0; }
  html, body {
    width: 1200px; height: 1023px; overflow: hidden;
    background: var(--backdrop);
    font-family: "Open Sans", Arial, sans-serif;
  }
  .sheet {
    width: 1200px; height: 1023px;
    display: flex; flex-direction: column; align-items: center; justify-content: center;
    gap: 40px;
  }
  .card {
    position: relative;
    width: 800px; height: 457px;
    border-radius: 26px;
    overflow: hidden;
    box-shadow: 0 8px 24px rgba(0,0,0,.18);
  }
  /* Front */
  .card-front { background: linear-gradient(160deg, #ffffff 0%, var(--card-white) 60%, #ececec 100%); }
  .card-front .swoosh { position: absolute; inset: 0; width: 100%; height: 100%; }
  .star-field {
    position: absolute;
    background: radial-gradient(ellipse at 70% 70%, rgba(224,22,142,.14), rgba(224,22,142,0) 70%);
  }
  .card-front .star-field { right: 0; bottom: 0; width: 420px; height: 300px; }
  .wordmark {
    font-family: "Open Sans", Arial, sans-serif;
    font-weight: 700;
    letter-spacing: -0.5px;
    display: flex; align-items: center; gap: 12px;
    white-space: nowrap;
  }
  .wordmark .mark-dot { display: inline-block; border-radius: 50%; }
  .card-front .wordmark {
    position: absolute; left: 48px; top: 28px;
    font-size: 36px; line-height: 1.2; color: var(--hot-pink);
  }
  .card-front .wordmark .mark-dot { width: 14px; height: 14px; background: var(--hot-pink); }
  .address {
    position: absolute; right: 52px; top: 120px;
    text-align: right; font-size: 20px; line-height: 1.4; color: var(--ink);
    font-style: normal;
  }
  .person { position: absolute; left: 48px; bottom: 30px; }
  .person-name { font-size: 24px; font-weight: 700; color: var(--hot-pink); line-height: 1.35; }
  .person-title { font-size: 20px; color: var(--grey-text); margin-bottom: 14px; line-height: 1.35; }
  .contact-list { list-style: none; }
  .contact-list li {
    display: flex; align-items: center; gap: 12px;
    font-size: 18px; color: var(--grey-text); line-height: 1.5;
  }
  .contact-list svg { width: 18px; height: 18px; flex: none; }
  /* Back */
  .card-back {
    background: linear-gradient(120deg, var(--pink-deep) 0%, var(--hot-pink) 45%, var(--pink-light) 70%, var(--hot-pink) 100%);
  }
  .card-back .wordmark {
    position: absolute; right: 60px; top: 70px;
    font-size: 62px; color: var(--ink);
  }
  .card-back .wordmark .mark-dot { width: 24px; height: 24px; background: var(--ink); }
  .card-back .star-field {
    left: 0; bottom: 0; width: 100%; height: 140px;
    background: linear-gradient(0deg, rgba(255,255,255,.22), rgba(255,255,255,0));
  }
</style>
</head>
<body>
<main class="sheet">

  <section class="card card-front" aria-label="Card front with contact details">
    <div class="star-field" role="img" aria-label="Faint pink star pattern"></div>
    <svg class="swoosh" viewBox="0 0 800 457" preserveAspectRatio="none" aria-hidden="true">
      <defs>
        <linearGradient id="swooshFill" x1="0" y1="1" x2="1" y2="0">
          <stop offset="0" stop-color="#c80a7c"/>
          <stop offset="0.5" stop-color="#e0168e"/>
          <stop offset="1" stop-color="#e34197"/>
        </linearGradient>
      </defs>
      <path d="M0 178 C 250 140, 500 90, 800 30 L 800 50 C 500 120, 250 180, 0 228 Z" fill="url(#swooshFill)"/>
    </svg>

    <div class="wordmark"><span class="mark-dot"></span>Staffwise Partners</div>

    <address class="address">P.O. Box 120,<br>Lakeview<br>NSW 2400</address>

    <div class="person">
      <p class="person-name">Claire Benton</p>
      <p class="person-title">Principal Consultant</p>
      <ul class="contact-list">
        <li>
          <svg viewBox="0 0 24 24" aria-hidden="true"><path fill="#e0168e" d="M6.6 10.8a15 15 0 0 0 6.6 6.6l2.2-2.2c.3-.3.7-.4 1-.2 1.1.4 2.3.6 3.6.6.6 0 1 .4 1 1V20c0 .6-.4 1-1 1A17 17 0 0 1 3 4c0-.6.4-1 1-1h3.5c.6 0 1 .4 1 1 0 1.300.2 2.500.6 3.600.1.3 0 .7-.2 1z"/></svg>
          02 6500 1234
        </li>
        <li>
          <svg viewBox="0 0 24 24" aria-hidden="true"><rect x="6" y="2" width="12" height="20" rx="2" fill="none" stroke="#e0168e" stroke-width="2"/><circle cx="12" cy="18" r="1.3" fill="#e0168e"/></svg>
          0400 123 456
        </li>
        <li>
          <svg viewBox="0 0 24 24" aria-hidden="true"><rect x="2" y="5" width="20" height="14" rx="1" fill="#e0168e"/><path d="M3 6l9 7 9-7" fill="none" stroke="#fff" stroke-width="1.6"/></svg>
          claire@staffwisepartners.com.au
        </li>
        <li>
          <svg viewBox="0 0 24 24" aria-hidden="true"><circle cx="12" cy="12" r="9" fill="#e0168e"/><path d="M3 12h18M12 3c3 3 3 15 0 18M12 3c-3 3-3 15 0 18" fill="none" stroke="#fff" stroke-width="1.3"/></svg>
          www.staffwisepartners.com.au
        </li>
      </ul>
    </div>
  </section>

  <section class="card card-back" aria-label="Card back with name">
    <div class="star-field" role="img" aria-label="Soft star pattern along the lower edge"></div>
    <div class="wordmark"><span class="mark-dot"></span>Staffwise Partners</div>
  </section>

</main>
</body>
</html>
```